Pediatric Practice Flyer Design

I need marketing flyer created for distribution. It is for a pediatric clinic. Need some realistic eye catching design and content. I already have a logo that will go on top of the flyer. I will be using corbelwade for flyer print service. So need it copyable for printing. Again, need eye catching content as well. We are planning on opening the clinic in December.

```html
<!DOCTYPE html>
<html lang="en">
<head>
<meta charset="utf-8">
<title>Maple Sprouts Pediatrics – Opening Flyer</title>
<link href="https://fonts.googleapis.com/css2?family=Poppins:wght@400;500;600;700;800&display=swap" rel="stylesheet">
<style>
  :root{
    --red:#e81e2b;
    --orange:#f7941d;
    --teal:#1ea89a;
    --teal-text:#17a096;
    --purple:#67308f;
    --blue:#1b70c0;
    --grey:#e4e4e4;
    --ink:#2a2a2a;
    --white:#ffffff;
  }
  *{margin:0;padding:0;box-sizing:border-box}
  html,body{width:783px;height:1200px;overflow:hidden;background:#f0f0f0}
  body{font-family:"Poppins",sans-serif;color:var(--ink)}
  .flyer{position:relative;width:783px;height:1200px;background:var(--white);overflow:hidden}
  .abs{position:absolute}
  .shapes{position:absolute;left:0;top:0}

  .brand{left:58px;top:58px;display:flex;align-items:center;gap:10px}
  .brand-dot{width:26px;height:26px;border-radius:50%;background:var(--orange)}
  .brand-name{font-weight:700;font-size:25px;color:var(--red);letter-spacing:-.3px}

  .welcome{left:64px;top:168px;color:var(--white)}
  .welcome-kicker{font-size:25px;font-weight:700;letter-spacing:.3px}
  .welcome-kicker span{font-weight:400}
  .welcome-name{font-size:46px;font-weight:800;line-height:1;margin-top:6px;letter-spacing:-1px}
  .welcome-sub{display:flex;align-items:center;gap:6px;margin-top:8px;font-size:17px;font-weight:700}
  .welcome-sub::before{content:"";width:160px;height:2px;background:var(--orange)}
  .opening{left:60px;top:308px;color:var(--white)}
  .opening-small{font-size:19px;font-weight:400}
  .opening-big{font-size:23px;font-weight:700;line-height:1.15}

  .intro{left:59px;top:398px;width:520px;font-size:12.3px;line-height:1.3}
  .goal-title{left:59px;top:425px;font-size:20px;font-weight:400}
  .goal-title b,.section-title b{color:var(--blue);font-weight:700}
  .goal-text{left:59px;top:456px;width:440px;font-size:12px;line-height:1.25}
  .checklist{left:59px;top:492px;display:flex;gap:28px;list-style:none;font-size:15px;font-weight:600}
  .checklist li{display:flex;align-items:center;gap:8px}

  .section-title{left:59px;top:572px;font-size:20px;font-weight:400}
  .doctor-photo{left:58px;top:610px;width:150px;height:136px;border:3px solid #fff;box-shadow:0 1px 4px rgba(0,0,0,.35)}
  .doctor-name{left:236px;top:615px;font-size:18px;font-weight:700;color:var(--teal-text)}
  .body-text{font-size:9.8px;line-height:13.6px;text-align:justify}
  .bio{left:236px;top:645px;width:499px}
  .recog{left:59px;top:757px;width:676px;text-align:left}
  .col-left{left:59px;top:800px;width:316px}
  .col-right{left:421px;top:800px;width:314px}
  .body-text p+p{margin-top:13px}

  .reg-title{left:421px;top:996px;font-size:18px;font-weight:700;color:var(--teal-text)}
  .field{left:421px;display:flex;align-items:flex-end;font-size:10.5px;font-weight:600;width:314px}
  .field span{width:98px}
  .field i{flex:1;border-bottom:1px solid #9a9a9a;height:1px;margin-bottom:3px}
  .f1{top:1024px}.f2{top:1054px}

  .register-tag{left:62px;top:1089px;font-size:18px;font-weight:600;color:var(--white)}
  .contact{left:62px;top:1128px;display:flex;align-items:center;gap:14px;color:var(--white)}
  .phone{display:flex;align-items:center;gap:4px;font-size:20px;font-weight:700}
  .email{display:flex;align-items:center;gap:5px;font-size:12px;font-weight:600}
  .web{left:482px;top:1128px;display:flex;align-items:center;gap:7px;color:var(--white);font-size:13px;font-weight:600;letter-spacing:.8px}
</style>
</head>
<body>
<main class="flyer">
  <svg class="shapes" width="783" height="1200" viewBox="0 0 783 1200" aria-hidden="false">
    <defs>
      <linearGradient id="photoTone" x1="0" y1="0" x2="1" y2="1">
        <stop offset="0" stop-color="#e9e6e2"/>
        <stop offset=".45" stop-color="#d7c6b4"/>
        <stop offset=".75" stop-color="#2f7fae"/>
        <stop offset="1" stop-color="#eef0f2"/>
      </linearGradient>
      <linearGradient id="babyTone" x1="0" y1="0" x2="1" y2="0">
        <stop offset="0" stop-color="#efe6d6"/>
        <stop offset="1" stop-color="#f3ddcf"/>
      </linearGradient>
      <linearGradient id="portraitTone" x1="0" y1="0" x2="1" y2="1">
        <stop offset="0" stop-color="#cfcac2"/>
        <stop offset=".5" stop-color="#3a3c44"/>
        <stop offset="1" stop-color="#6f8a55"/>
      </linearGradient>
    </defs>

    <rect x="0" y="380" width="783" height="172" fill="var(--grey)"/>
    <polygon points="0,149 423,149 552,374 0,374" fill="var(--red)"/>

    <polygon points="374,0 783,0 783,560 696,560" fill="url(#photoTone)" role="img" aria-label="Photo of a smiling pediatrician in blue scrubs showing a tablet to a mother holding her young daughter"/>
    <rect x="498" y="486" width="262" height="154" rx="60" fill="url(#babyTone)" role="img" aria-label="Photo of a baby holding a stethoscope to a teddy bear"/>

    <line x1="361" y1="0" x2="592" y2="398" stroke="var(--orange)" stroke-width="3"/>
    <line x1="783" y1="312" x2="702" y2="470" stroke="var(--orange)" stroke-width="3"/>
    <polyline points="714,448 742,500 783,420" fill="none" stroke="var(--red)" stroke-width="6"/>
    <line x1="282" y1="586" x2="505" y2="586" stroke="var(--orange)" stroke-width="2"/>

    <polygon points="0,1108 410,1108 490,1200 0,1200" fill="var(--teal)"/>
    <polygon points="432,1108 783,1108 783,1176 498,1176" fill="var(--purple)"/>
    <polygon points="56,1083 246,1083 262,1112 56,1112" fill="var(--red)"/>
  </svg>

  <div class="abs doctor-photo" role="img" aria-label="Portrait photo of Dr. Nadia Rahimi standing outside a building" style="background:linear-gradient(135deg,#d2cdc5,#3a3c44 55%,#6f8a55)"></div>

  <header class="abs brand">
    <span class="brand-dot"></span>
    <span class="brand-name">Maple Sprouts Pediatrics</span>
  </header>

  <section class="abs welcome">
    <div class="welcome-kicker">WELCOME <span>TO</span></div>
    <div class="welcome-name">Maple Sprouts</div>
    <div class="welcome-sub">CARE PEDIATRIC!</div>
  </section>
  <section class="abs opening">
    <div class="opening-small">WE ARE PLANNING ON</div>
    <div class="opening-big">OPENING THE CLINIC IN DECEMBER.</div>
  </section>

  <p class="abs intro">Where we believe it takes a community to raise a child. We are excited to be small yet important member of the community to help raise a healthy and happy child.</p>
  <h2 class="abs goal-title">OUR <b>GOAL</b></h2>
  <p class="abs goal-text">Our goal is to provide personalized and comprehensive care collectively that consists of the</p>
  <ul class="abs checklist">
    <li><svg width="14" height="14" viewBox="0 0 14 14"><circle cx="7" cy="7" r="7" fill="var(--red)"/><path d="M3.8 7.2l2.2 2.1 4.2-4.4" fill="none" stroke="#fff" stroke-width="1.8"/></svg>Parent</li>
    <li><svg width="14" height="14" viewBox="0 0 14 14"><circle cx="7" cy="7" r="7" fill="var(--red)"/><path d="M3.8 7.2l2.2 2.1 4.2-4.4" fill="none" stroke="#fff" stroke-width="1.8"/></svg>Child</li>
    <li><svg width="14" height="14" viewBox="0 0 14 14"><circle cx="7" cy="7" r="7" fill="var(--red)"/><path d="M3.8 7.2l2.2 2.1 4.2-4.4" fill="none" stroke="#fff" stroke-width="1.8"/></svg>Provider Triangle</li>
  </ul>

  <h2 class="abs section-title">MEET OUR <b>PROVIDER</b></h2>
  <h3 class="abs doctor-name">Dr. Nadia Rahimi</h3>
  <p class="abs body-text bio">Dr. Nadia Rahimi is an experienced and qualified Pediatrician, previously served the communities of Oakridge and Fairview for several years. She obtained her medical degree from the Crescent Valley Medical College. After numerous research and observership positions at the Linden Clinic, Harbor Care Alliance and Eastbrook University, and at Bayview Children's Hospital and Riverside General, she decided to pursue her passion of working with children and trained in Pediatrics at Westfield Health Sciences Center in Pinecrest.</p>
  <p class="abs body-text recog">Where she was recognized in the Metro Living Top Doctors 2019 magazine as well as Top Female Doctor in the city of Oakridge. For past few years she had been serving the underserved population of Millbrook.</p>

  <div class="abs body-text col-left">
    <p>She obtained her medical degree from the Crescent Valley Medical College. After numerous research and observership positions at the Linden Clinic, Harbor Care Alliance and Eastbrook University, and at Bayview Children's Hospital and Riverside General, she decided to pursue her passion of working with children and trained in Pediatrics at Westfield Health Sciences Center in Pinecrest.</p>
    <p>A devout mother of five, Dr Rahimi recognizes the special care and attention that children need and exercises her professional and maternal insight with her patients. She is multilingual in English, Hindi and Punjabi allowing patients from a variety of backgrounds to comfortably communicate with her. Her extensive travel has also allowed her to be sensitive to various cultures and is able to exercises her professional and maternal insight with her patients.</p>
  </div>
  <div class="abs body-text col-right">
    <p>She is multilingual in English, Hindi and Punjabi allowing patients from a variety of backgrounds to comfortably communicate with her. Her extensive travel has also allowed her to be sensitive to various cultures and is able to understand the needs of patients from different backgrounds. Caring for children is her passion.</p>
    <p>She believes that a visit to a Pediatrician should be warm and friendly and ensure an environment of comfort, diligence, discussion, and education. She also believes in building a relationship with the Patient/Parent by listening and creating a partnership to maintain and improve lifelong health.</p>
  </div>

  <h3 class="abs reg-title">New Patient Registration</h3>
  <div class="abs field f1"><span>Your Full Name:</span><i></i></div>
  <div class="abs field f2"><span>Phone Number:</span><i></i></div>

  <div class="abs register-tag">REGISTER TODAY</div>
  <footer>
    <div class="abs contact">
      <span class="phone"><svg width="15" height="15" viewBox="0 0 24 24"><path d="M6.6 10.8a15 15 0 0 0 6.6 6.6l2.2-2.2a1 1 0 0 1 1-.25 11.4 11.4 0 0 0 3.6.57 1 1 0 0 1 1 1V20a1 1 0 0 1-1 1A17 17 0 0 1 3 4a1 1 0 0 1 1-1h3.5a1 1 0 0 1 1 1c0 1.25.2 2.45.57 3.57a1 1 0 0 1-.25 1z" fill="#fff"/></svg>555.014.2270</span>
      <span class="email"><svg width="13" height="10" viewBox="0 0 13 10"><rect x=".5" y=".5" width="12" height="9" fill="none" stroke="#fff"/><path d="M.5.5l6 5 6-5" fill="none" stroke="#fff"/></svg>hello@maplesproutskids.com</span>
    </div>
    <div class="abs web"><svg width="14" height="14" viewBox="0 0 14 14"><circle cx="7" cy="7" r="6" fill="none" stroke="var(--teal)" stroke-width="1.4"/><path d="M1 7h12M7 1c-3 3-3 9 0 12M7 1c3 3 3 9 0 12" fill="none" stroke="var(--teal)" stroke-width="1.1"/></svg>www.maplesproutskids.com</div>
  </footer>
</main>
</body>
</html>
```